business card for author of crime novel

I am an author with a new book. I need a business card with the book's cover on one side (already uploaded), and contact details on the other.

Tom Velasquin
Author

telephone: 917-555-0162
website: www.tomvelasquin.example
facebook: facebook.com/tvelasquin
twitter: twitter.com/tvelasquin
email: tvelasquin@mailbox.example

Target Market(s)

Readers of mystery books

Industry/Entity Type

Business

Contact Information for Business Card

Tom Velasquin
Author

telephone: 917-555-0162

Font styles to use
Serif
Sans Serif

Requirements
Must have
• Book cover on one side. My contact info on the other, with the name of the book repeated if that makes sense. Clean design.
Should not have
• Overly ornate, too formal, too distracting

```html
<!DOCTYPE html>
<html lang="en">
<head>
<meta charset="utf-8">
<title>Tom Velasquin – Author Business Card</title>
<link rel="stylesheet" href="https://fonts.googleapis.com/css2?family=Cardo&family=Open+Sans:wght@300;400&display=swap">
<style>
  :root {
    --page-bg: #cfcfcf;
    --card-slate: #2f3f49;
    --card-text: #f2f2f0;
    --rule: #7f8b92;
    --book-orange: #e3a42b;
    --book-orange-dark: #b9801c;
    --book-teal: #6f8a92;
    --book-sky: #9fd3e0;
    --book-sky-dark: #6e9fae;
    --book-scene: #6f7a5a;
    --page-edge: #e6dcc4;
  }
  * { margin: 0; padding: 0; box-sizing: border-box; }
  html, body { width: 1200px; height: 1200px; overflow: hidden; }
  body {
    background: var(--page-bg);
    display: flex;
    flex-direction: column;
    align-items: center;
    justify-content: center;
    gap: 60px;
  }
  .card {
    position: relative;
    width: 880px;
    height: 500px;
    background: var(--card-slate);
    color: var(--card-text);
    overflow: hidden;
    box-shadow: 0 6px 18px rgba(0,0,0,0.18);
  }
  .author-name {
    font-family: "Cardo", Georgia, serif;
    font-weight: 400;
    letter-spacing: 0.5px;
    white-space: nowrap;
  }
  .author-role {
    font-family: "Cardo", Georgia, serif;
    letter-spacing: 1px;
  }

  /* Contact side */
  .contact-side .identity {
    position: absolute;
    left: 70px;
    top: 70px;
    width: 330px;
    padding-bottom: 10px;
    border-bottom: 1px solid var(--rule);
  }
  .contact-side .author-name { font-size: 40px; line-height: 1.1; }
  .contact-side .author-role { font-size: 36px; line-height: 1.1; }
  .contact-list {
    position: absolute;
    left: 70px;
    top: 250px;
    list-style: none;
    font-family: "Open Sans", Arial, sans-serif;
    font-weight: 300;
    font-size: 26px;
    line-height: 1.3;
    white-space: nowrap;
  }
  .cover-corner {
    position: absolute;
    right: -40px;
    top: -30px;
    width: 420px;
    height: 240px;
  }

  /* Cover side */
  .cover-side .book-stack {
    position: absolute;
    left: 120px;
    top: 40px;
    width: 260px;
    height: 430px;
  }
  .cover-side .identity {
    position: absolute;
    left: 470px;
    top: 250px;
    width: 330px;
    text-align: center;
  }
  .cover-side .author-name {
    font-size: 42px;
    padding-bottom: 8px;
    border-bottom: 1px solid var(--rule);
  }
  .cover-side .author-role { font-size: 38px; margin-top: 4px; }
</style>
</head>
<body>

  <section class="card contact-side">
    <div class="identity">
      <div class="author-name">Tom Velasquin</div>
      <div class="author-role">Author</div>
    </div>
    <ul class="contact-list">
      <li>917-555-0162</li>
      <li>www.tomvelasquin.example</li>
      <li>friendsphere.example/tvelasquin</li>
      <li>chirpline.example/tvelasquin</li>
      <li>tvelasquin@mailbox.example</li>
    </ul>
    <svg class="cover-corner" viewBox="0 0 420 240" role="img" aria-label="Corner of the hardcover book Dead Letter Alley, orange binding with city building cover art">
      <polygon points="20,0 420,0 420,230 90,230" fill="var(--book-orange-dark)"/>
      <polygon points="10,0 420,0 420,215 80,215" fill="var(--book-orange)"/>
      <polygon points="60,0 400,0 400,175 110,175" fill="var(--book-teal)"/>
      <polygon points="80,215 420,215 420,240 90,240" fill="var(--page-edge)"/>
    </svg>
  </section>

  <section class="card cover-side">
    <svg class="book-stack" viewBox="0 0 260 430" role="img" aria-label="Two hardcover books: Dead Letter Alley in orange and Final Ink in pale blue, both A Marlow Keene Mystery">
      <rect x="20" y="0" width="180" height="260" fill="var(--book-orange-dark)"/>
      <rect x="10" y="6" width="180" height="254" fill="var(--book-orange)"/>
      <rect x="30" y="40" width="140" height="170" fill="var(--book-teal)"/>
      <rect x="60" y="240" width="190" height="190" fill="var(--book-sky-dark)"/>
      <rect x="50" y="246" width="190" height="178" fill="var(--book-sky)"/>
      <rect x="68" y="280" width="154" height="104" fill="var(--book-scene)"/>
    </svg>
    <div class="identity">
      <div class="author-name">Tom Velasquin</div>
      <div class="author-role">Author</div>
    </div>
  </section>

</body>
</html>
```